" Ela ainda não está funcionando, mas a ideia é ser uma loja virtual com todas as informações e facilidades para locação de cadeirinhas infantis, carrinhos, tapetinhos, brinquedos, cadeiras de automóveis, etc. Todos os itens serão entregues e recolhidos nos endereços informados pelos clientes. A principal ideia é facilitar a vida das mães que viajam com crianças pequenas. É sempre muito trabalhoso carregar toda a tralha infantil, portanto facilitaremos a vida locando todos os equipamentos no destino, entregando e recolhendo em qualquer localidade de Belo Horizonte. Praticidade, facilidade e comodidade para as mães que precisem de itens essenciais para o dia a dia dos bebês. "

```html
<!DOCTYPE html>
<html lang="pt-BR">
<head>
<meta charset="utf-8">
<title>Malinha Kids – Flyer</title>
<link href="https://fonts.googleapis.com/css2?family=Nunito:wght@600;700;800;900&display=swap" rel="stylesheet">
<style>
  :root {
    --bg: #e4e4e2;
    --sky: #1f9ad9;
    --gold: #c99a2e;
    --gold-text: #c7972a;
    --navy: #1a7fc4;
    --paper: #ffffff;
    --skin-light: #f3d2bb;
    --skin-mid: #e2b497;
  }
  * { margin: 0; padding: 0; box-sizing: border-box; }
  html, body { width: 1200px; height: 1200px; overflow: hidden; }
  body {
    background: var(--bg);
    font-family: "Nunito", sans-serif;
    display: flex; align-items: center; justify-content: center;
  }
  .flyer {
    position: relative;
    width: 1100px; height: 760px;
    background: var(--sky);
    overflow: hidden;
    box-shadow: 0 6px 20px rgba(0,0,0,.12);
  }
  .flyer__shapes { position: absolute; inset: 0; }
  .flyer__photo { position: absolute; left: 520px; top: 320px; width: 400px; height: 440px; }
  .brand {
    position: absolute; left: 250px; top: 56px;
    display: flex; align-items: center; gap: 12px;
    font-weight: 900; font-size: 34px; color: var(--gold-text);
  }
  .brand__dot { width: 22px; height: 22px; border-radius: 50%; background: var(--sky); }
  .services {
    position: absolute; left: 70px; top: 150px;
    color: var(--gold-text); font-weight: 700; font-size: 23px; line-height: 1.3;
  }
  .services__title { font-weight: 800; margin-bottom: 12px; }
  .services__list { list-style: none; }
  .contact { position: absolute; left: 70px; top: 396px; color: var(--navy); }
  .contact__title { font-weight: 900; font-size: 36px; letter-spacing: .5px; }
  .contact__phone { font-weight: 800; font-size: 24px; margin-top: 10px; }
  .contact__email { font-weight: 800; font-size: 19px; margin-top: 2px; }
  .headline {
    position: absolute; left: 640px; top: 70px; width: 420px;
    color: var(--paper); font-weight: 900; font-size: 35px; line-height: 1.2;
    text-align: center;
  }
</style>
</head>
<body>
  <article class="flyer">
    <svg class="flyer__shapes" viewBox="0 0 1100 760" width="1100" height="760" aria-hidden="true">
      <path d="M0,0 H625 C615,390 485,665 0,735 Z" fill="var(--gold)"/>
      <path d="M0,0 H610 C600,380 470,650 0,720 Z" fill="var(--paper)"/>
    </svg>

    <svg class="flyer__photo" viewBox="0 0 420 460" width="400" height="440" role="img" aria-label="Fotografia de um bebê sorridente mandando beijo">
      <defs>
        <radialGradient id="photoTone" cx="50%" cy="40%" r="60%">
          <stop offset="0%" stop-color="var(--skin-light)"/>
          <stop offset="100%" stop-color="var(--skin-mid)"/>
        </radialGradient>
      </defs>
      <path d="M60,460 C40,360 90,300 150,290 C120,200 150,40 250,40 C350,40 380,200 320,290 C380,310 420,380 410,460 Z" fill="url(#photoTone)"/>
    </svg>

    <div class="brand"><span class="brand__dot"></span>Malinha Kids</div>

    <section class="services">
      <p class="services__title">Locação de:</p>
      <ul class="services__list">
        <li>Cadeirinha de bebê</li>
        <li>Cadeirinha para veículos</li>
        <li>Brinquedos Diversos</li>
        <li>Andador</li>
        <li>Cadeirinha balanço</li>
        <li>Chiqueirinho</li>
      </ul>
    </section>

    <section class="contact">
      <p class="contact__title">FALE CONOSCO</p>
      <p class="contact__phone">(31) 90000-4521</p>
      <p class="contact__email">CONTATO@MALINHAKIDS.COM.BR</p>
    </section>

    <h1 class="headline">Locação de itens infantis para facilitar seu dia a dia e sua vida!</h1>
  </article>
</body>
</html>
```